Flyer for internet links

I need to develop a concept to send in a mailout campaign (stationery). I has to be in A5 size (half A4 page), double sided.
On one side it should have the Corvalo's logo (attached in HR), plus the captions: "Business grade Internet links at prices never seen before" plus a related picture.
On the other side it should show the text attached in the file "Text.doc".
Please let me know if you have any questions.

```html
<!DOCTYPE html>
<html lang="en">
<head>
<meta charset="utf-8">
<title>Corvalo – Business Grade Internet Flyer</title>
<link rel="stylesheet" href="https://fonts.googleapis.com/css2?family=Kanit:wght@600;700&family=Oswald:wght@600&family=Open+Sans:ital,wght@0,400;0,600;1,400&display=swap">
<style>
  :root {
    --canvas: #e6e6e6;
    --paper: #ffffff;
    --blue: #2a7de1;
    --blue-deep: #1a5fb8;
    --grey-ink: #5a5a5a;
    --dark-ink: #333a45;
    --navy: #14306b;
    --photo-a: #bfe8e4;
    --photo-b: #7fb3c9;
    --photo-c: #d9dde2;
    --photo-d: #8c9aa8;
    --rule: #6b6b6b;
  }
  * { box-sizing: border-box; margin: 0; padding: 0; }
  html, body { width: 1200px; height: 1000px; overflow: hidden; }
  body { background: var(--canvas); font-family: "Open Sans", sans-serif; position: relative; }

  .flyer {
    position: absolute; width: 640px; height: 440px;
    background: var(--paper); overflow: hidden;
    box-shadow: 0 6px 18px rgba(0,0,0,.18);
  }
  .flyer--front { left: 140px; top: 50px; }
  .flyer--back  { left: 420px; top: 510px; }
  .flyer__art { position: absolute; inset: 0; }

  .headline { position: absolute; font-family: "Kanit", sans-serif; font-weight: 700; text-transform: uppercase; line-height: 1.02; }
  .headline .blue { color: var(--blue); }
  .headline .grey { color: var(--grey-ink); }
  .flyer--front .headline { left: 30px; top: 38px; }
  .flyer--front .headline span { display: block; }
  .flyer--front .l1 { font-size: 30px; }
  .flyer--front .l2 { font-size: 23px; }
  .flyer--front .l3, .flyer--front .l4, .flyer--front .l5 { font-size: 20px; }
  .flyer--front .l4, .flyer--front .l5 { padding-left: 26px; }
  .flyer--front .l3 { padding-left: 6px; }

  .brand { position: absolute; display: flex; align-items: center; gap: 8px; }
  .brand__dot { width: 30px; height: 30px; border-radius: 50%; background: var(--blue); }
  .brand__name { font-family: "Kanit", sans-serif; font-weight: 600; color: var(--navy); font-size: 30px; line-height: 1; }
  .flyer--front .brand { left: 48px; top: 370px; }
  .flyer--back .brand { left: 36px; top: 392px; }
  .flyer--back .brand__dot { width: 22px; height: 22px; }
  .flyer--back .brand__name { font-size: 24px; }

  .about { position: absolute; left: 282px; top: 318px; width: 338px; color: var(--dark-ink); }
  .about__title { font-size: 14px; color: var(--blue); text-decoration: underline; font-weight: 400; margin-bottom: 5px; }
  .about p { font-size: 7.4px; line-height: 1.45; margin-bottom: 5px; }

  .flyer--back .headline { left: 26px; top: 36px; font-size: 20px; }
  .flyer--back .headline span { display: block; }
  .flyer--back .headline .l3 { padding-left: 12px; }

  .plans { position: absolute; left: 48px; top: 128px; display: grid; grid-template-columns: 96px 96px; gap: 12px 14px; }
  .plan {
    width: 96px; height: 96px; background: var(--blue); color: #fff;
    text-align: center; padding-top: 10px;
  }
  .plan__speed { font-family: "Oswald", sans-serif; font-weight: 600; font-size: 20px; line-height: 1; }
  .plan__type { font-size: 5.5px; text-transform: uppercase; margin: 2px 0 10px; letter-spacing: .2px; }
  .plan__terms { font-size: 8px; line-height: 1.3; }

  .contact-note { position: absolute; left: 72px; top: 334px; font-size: 7px; font-style: italic; color: var(--grey-ink); }
  .contact { position: absolute; left: 182px; top: 350px; font-size: 9.5px; color: var(--dark-ink); line-height: 1.35; }
  .contact__company { color: var(--blue); font-size: 10.5px; margin-bottom: 5px; }
  .contact__row { display: flex; align-items: center; gap: 5px; font-size: 8.5px; }
  .contact__row svg { width: 9px; height: 9px; fill: var(--blue); flex: none; }
</style>
</head>
<body>

<section class="flyer flyer--front">
  <svg class="flyer__art" viewBox="0 0 640 440" width="640" height="440">
    <defs>
      <linearGradient id="frontPhoto" x1="0" y1="0" x2="1" y2="1">
        <stop offset="0" stop-color="var(--photo-a)"/>
        <stop offset="1" stop-color="var(--photo-b)"/>
      </linearGradient>
      <radialGradient id="globeTone" cx=".4" cy=".4" r=".7">
        <stop offset="0" stop-color="#9fd3f5"/>
        <stop offset="1" stop-color="#1b5aa8"/>
      </radialGradient>
    </defs>
    <path role="img" aria-label="Photo: smiling businessman in a suit using a tablet, with video-call contact bubbles floating beside him"
          d="M292,0 L640,0 L640,268 Q440,300 242,302 Q228,140 292,0 Z" fill="url(#frontPhoto)"/>
    <path d="M284,0 Q220,150 234,304" fill="none" stroke="var(--blue)" stroke-width="3"/>
    <path d="M0,262 Q130,310 300,302 Q480,292 640,258" fill="none" stroke="var(--blue)" stroke-width="2"/>
    <path d="M0,270 Q130,318 300,310 Q480,300 640,266" fill="none" stroke="var(--rule)" stroke-width="2.5"/>
    <path d="M272,310 Q262,380 266,440" fill="none" stroke="var(--rule)" stroke-width="2"/>
    <circle role="img" aria-label="Illustration: glowing blue globe with network links" cx="100" cy="258" r="52" fill="url(#globeTone)" stroke="var(--rule)" stroke-width="4"/>
  </svg>

  <h1 class="headline">
    <span class="l1 blue">Business</span>
    <span class="l2 grey">Grade Internet</span>
    <span class="l3 blue">Links at prices</span>
    <span class="l4 grey">Never</span>
    <span class="l5 blue">Seen before</span>
  </h1>

  <div class="brand"><span class="brand__dot"></span><span class="brand__name">Corvalo</span></div>

  <div class="about">
    <h2 class="about__title">About Corvalo</h2>
    <p>Founded in 2002, Corvalo has been a leading provider of IT services and solutions to Australian businesses. Corvalo helps organisations use technology to increase productivity, reduce costs, minimise risks and grow strategically.</p>
    <p>Organisations turn to Corvalo when they need their IT infrastructure, software engineering and IT projects delivered on time, on budget and cannot achieve this with their current internal resources.</p>
  </div>
</section>

<section class="flyer flyer--back">
  <svg class="flyer__art" viewBox="0 0 640 440" width="640" height="440">
    <defs>
      <linearGradient id="backPhoto" x1="0" y1="0" x2="1" y2="1">
        <stop offset="0" stop-color="var(--photo-c)"/>
        <stop offset="1" stop-color="var(--photo-d)"/>
      </linearGradient>
    </defs>
    <path role="img" aria-label="Photo: senior manager guiding young colleagues working at computers in an office"
          d="M300,0 L640,0 L640,440 L370,440 Q246,230 300,0 Z" fill="url(#backPhoto)"/>
    <path d="M292,0 Q238,230 360,440" fill="none" stroke="var(--blue)" stroke-width="2.5"/>
  </svg>

  <h1 class="headline">
    <span class="l1 blue">Business grade internet</span>
    <span class="l2 grey">Links at prices</span>
    <span class="l3 blue">Never seen before</span>
  </h1>

  <div class="plans">
    <div class="plan">
      <div class="plan__speed">400 MBPS</div>
      <div class="plan__type">Fibre for under</div>
      <div class="plan__terms">$400/Month,<br>36 Months,<br>$2500 Installation Fees</div>
    </div>
    <div class="plan">
      <div class="plan__speed">100 MBPS</div>
      <div class="plan__type">Fibre for under</div>
      <div class="plan__terms">$300/Month,<br>36 Months,<br>$5500 Installation Fees</div>
    </div>
    <div class="plan">
      <div class="plan__speed">20 MBPS</div>
      <div class="plan__type">EFM (avg speed) for under</div>
      <div class="plan__terms">$300/Month,<br>36 Months,<br>No Installation Fees</div>
    </div>
    <div class="plan">
      <div class="plan__speed">10 MBPS</div>
      <div class="plan__type">EFM (avg speed) for under</div>
      <div class="plan__terms">$200/Month,<br>36 Months,<br>No Installation Fees</div>
    </div>
  </div>

  <p class="contact-note">For a detailed &amp; firm quote and site qualification, please contact:</p>

  <div class="brand"><span class="brand__dot"></span><span class="brand__name">Corvalo</span></div>

  <div class="contact">
    <div class="contact__name">DANA WHITFIELD</div>
    <div class="contact__company">Corvalo Pty Ltd.</div>
    <div class="contact__row">
      <svg viewBox="0 0 24 24"><path d="M6.6 10.8a15.1 15.1 0 0 0 6.6 6.6l2.2-2.2a1 1 0 0 1 1-.25 11.4 11.4 0 0 0 3.6.57 1 1 0 0 1 1 1V20a1 1 0 0 1-1 1A17 17 0 0 1 3 4a1 1 0 0 1 1-1h3.5a1 1 0 0 1 1 1c0 1.25.2 2.45.57 3.57a1 1 0 0 1-.25 1z"/></svg>
      <span>(02) 5550 1234</span>
    </div>
    <div class="contact__row">
      <svg viewBox="0 0 24 24"><path d="M2 5h20v14H2z M2 5l10 8 10-8" fill="var(--blue)" stroke="#fff" stroke-width="1.5"/></svg>
      <span>Dana.Whitfield@corvalo.com.au</span>
    </div>
  </div>
</section>

</body>
</html>
```